Stonebell Inc Ad Design, trying to attract new customers

Please see attached pictures and files for information
We are a Class A - Residential General Contractor in Lynchburg, VA with Master HVAC and Master PLUMBING Licenses. We focus on Water and Air Solutions for property owners.
We build, remodel, and repair homes
We do HVAC, including Humidity Control and Air Purification
We do Plumbing
We love to fix Water Leaks for Plumbing, Roof Leaks, Skylight Leaks, Basement Leaks, Foundation Leaks, Door and Window Leaks
We solve water and air issues on the outside of properties with custom structures, grading, and landscaping

Target Market(s)

Residential and Light Commercial property owners

Industry/Entity Type

Construction

Font styles to use
Other font styles liked:
• see cards

Colors
0054AA
0677BA
7BADD7
CADEEF
E8F1F8
00AB8E
00BBA5
67D7C9
C6EFE9
E9F9F6

Requirements
Must have
• See business cards
Nice to have
• see business cards
Should not have
• My name

```html
<!DOCTYPE html>
<html lang="en">
<head>
<meta charset="utf-8">
<title>Stonebell Inc – Billboard Ad</title>
<link rel="stylesheet" href="https://fonts.googleapis.com/css2?family=Poppins:wght@600;700;800&display=swap">
<style>
  :root {
    --page-bg: #eef1f4;
    --ad-bg: #ffffff;
    --green-dark-a: #2a8a3a;
    --green-dark-b: #3ea142;
    --green-light-a: #5fab38;
    --green-light-b: #80c245;
    --band-blue: #0677BA;
    --quote-light: #7fcdf2;
    --contact-blue: #0054AA;
    --phone-blue: #0a5fb4;
    --white: #ffffff;
  }
  * { box-sizing: border-box; margin: 0; padding: 0; }
  html, body {
    width: 1118px; height: 1200px; overflow: hidden;
    background: var(--page-bg);
    font-family: "Poppins", Arial, sans-serif;
  }
  .ad {
    position: absolute; left: 0; top: 432px;
    width: 1118px; height: 335px;
    background: var(--ad-bg);
    overflow: hidden;
  }
  .brand {
    position: absolute; left: 56px; top: 58px;
    display: flex; align-items: center; gap: 8px;
    color: var(--band-blue); font-weight: 800; font-size: 26px; letter-spacing: 1px;
  }
  .brand-dot { width: 22px; height: 22px; border-radius: 50%; background: var(--green-light-a); }
  .service {
    position: absolute; height: 77px; border-radius: 39px;
    display: flex; align-items: center; justify-content: center;
    color: var(--white); font-weight: 700; font-size: 21px; white-space: nowrap;
  }
  .service--dark { background: linear-gradient(90deg, var(--green-dark-a), var(--green-dark-b)); }
  .service--light { background: linear-gradient(90deg, var(--green-light-a), var(--green-light-b)); }
  .service--plumbing { left: 270px; top: 41px; width: 246px; justify-content: flex-start; padding-left: 32px; }
  .service--hvac { left: 19px; top: 134px; width: 236px; }
  .service--builds { left: 270px; top: 134px; width: 236px; }
  .service--leaks { left: 19px; top: 226px; width: 185px; }
  .service--landscape { left: 220px; top: 226px; width: 294px; justify-content: flex-start; padding-left: 28px; }
  .slogan-band {
    position: absolute; left: 588px; top: 45px; width: 530px; height: 138px;
    background: var(--band-blue);
    padding: 20px 0 0 16px;
    font-weight: 800; font-size: 42px; line-height: 50px; letter-spacing: -1.5px;
    color: var(--quote-light); white-space: nowrap;
  }
  .slogan-band .slogan-strong { color: var(--white); }
  .slogan-band .slogan-line2 { display: block; padding-left: 22px; }
  .contact-line {
    position: absolute; left: 614px; top: 207px;
    display: flex; align-items: center; gap: 10px;
    color: var(--contact-blue); font-weight: 600; font-size: 16px;
  }
  .contact-divider { width: 2px; height: 26px; background: var(--contact-blue); }
  .phone {
    position: absolute; left: 674px; top: 236px;
    color: var(--phone-blue); font-weight: 700; font-size: 52px; letter-spacing: -1px; line-height: 66px;
  }
  .technician-photo {
    position: absolute; left: 516px; top: 22px; width: 70px; height: 313px;
    border-radius: 34px 34px 0 0;
    background: linear-gradient(180deg, #2a4fa8 0%, #1d46c9 45%, #c9a871 70%, #1d3fb8 100%);
  }
</style>
</head>
<body>
  <main class="ad">
    <div class="brand"><span class="brand-dot"></span><span class="brand-name">STONEBELL</span></div>

    <div class="service service--light service--plumbing">Plumbing Repairs</div>
    <div class="service service--dark service--hvac">HVAC Solutions</div>
    <div class="service service--light service--builds">Custom Builds</div>
    <div class="service service--dark service--leaks">Leak Fixes</div>
    <div class="service service--light service--landscape">Landscaping &amp; Grading</div>

    <div class="slogan-band">“WE PUT <span class="slogan-strong">WATER &amp; AIR</span><span class="slogan-line2">IN THEIR PLACE”</span></div>

    <div class="contact-line">
      <span>Contact@StonebellVA.com</span>
      <span class="contact-divider"></span>
      <span>www.CoolCornerVA.com</span>
    </div>
    <div class="phone">(434) 555-0187</div>

    <div class="technician-photo" role="img" aria-label="Smiling technician in blue coveralls and cap wearing a tool belt, pointing at the viewer"></div>
  </main>
</body>
</html>
```